Club sale for moms — 3 static banners

Lullavo is the largest daily deal site for moms, kids and babies in Russia, which provides offers with discounts up to 70%.
We need 3 banners for our flash sale, all banners must be on a white background, all must be static and be in 2 versions, so when you hover over banner the picture changes. Banners' style should differ from other banners which refer to deals (like pebbloo's banners "Invite a friend, earn $20", they are attached).
Purpose: filling the empty space on the main page in case of absence of the necessary number of deals' banners. The example of our main page is attached.
1st static banner:
474px × 308px
text: Пригласите друга — получите бонус на следующую покупку!
That text means: Invite a friend and get a bonus for shopping.
After clicking on that banner a client will go to the site section "Invites".
The text means: Invite a friend and get a bonus for shopping.
2nd static banner:
308px × 199px
Text: Доставка по всей России. Оплата при получении.
After clicking on that banner a client will go to the site section about delivery.
The text means: Delivery all over Russia, pay on getting.
3rd static banner:
308px × 199px
Text:
Гарантия лучшей цены!
The text means:
Best price guarantee
Target Market(s)
moms
Industry/Entity Type
Club
Look and feel
Each slider illustrates characteristics of the customer's brand and the style your logo design should communicate.

```html
<!DOCTYPE html>
<html lang="ru">
<head>
<meta charset="utf-8">
<title>Lullavo — баннеры</title>
<link href="https://fonts.googleapis.com/css2?family=Open+Sans:wght@400;700&display=swap" rel="stylesheet">
<style>
  :root {
    --stage: #2b2b2b;
    --paper: #ffffff;
    --accent: #d6127d;
    --accent-dark: #b80c68;
    --ink-soft: #8a8a8a;
    --line: #8e8e8e;
    --field-border: #d4d4d4;
  }
  * { margin: 0; padding: 0; box-sizing: border-box; }
  html, body { width: 1200px; height: 723px; overflow: hidden; }
  body {
    background: var(--stage);
    font-family: "Open Sans", Arial, sans-serif;
    position: relative;
  }
  .banner {
    position: absolute;
    background: var(--paper);
    overflow: hidden;
  }
  .banner--invite { left: 146px; top: 93px; width: 429px; height: 522px; }
  .banner--delivery { left: 624px; top: 93px; width: 337px; height: 218px; }
  .banner--price { left: 624px; top: 354px; width: 337px; height: 217px; }

  .invite-title {
    position: absolute; left: 0; right: 0; top: 8px;
    text-align: center; color: var(--accent);
    font-weight: 700; font-size: 42px; line-height: 1.1; letter-spacing: -0.5px;
    white-space: nowrap;
  }
  .invite-subtitle {
    position: absolute; left: 0; right: 0; top: 57px;
    text-align: center; color: var(--accent);
    font-size: 19px; line-height: 1.2; white-space: nowrap;
  }
  .photo {
    position: absolute; border-radius: 40% 40% 12% 12%;
  }
  .photo--kids {
    left: 90px; top: 92px; width: 260px; height: 346px;
    background: linear-gradient(180deg, #f4e3d6 0%, #e9cdb8 30%, #e7b9a0 55%, #d83a3a 72%, #d9c8a6 86%, #f2efe9 100%);
    opacity: .85;
  }
  .photo--girl-standing {
    left: 204px; top: 11px; width: 121px; height: 207px;
    background: linear-gradient(180deg, #f2d9b4 0%, #efd1b5 28%, #5fc4a0 50%, #3fb892 85%, #9fdcc4 100%);
  }
  .photo--girl-sitting {
    left: 2px; top: 8px; width: 141px; height: 209px;
    background: linear-gradient(180deg, #f0cfa0 0%, #f1d5bd 30%, #5cc6a2 55%, #45b894 85%, #a7dfca 100%);
  }

  .email-form {
    position: absolute; left: 36px; top: 446px; width: 358px; height: 56px;
    display: flex; border: 1px solid var(--field-border); border-radius: 4px;
    box-shadow: 0 3px 5px rgba(0,0,0,.22); background: var(--paper); overflow: hidden;
  }
  .email-field {
    flex: 1; display: flex; align-items: center; padding-left: 19px;
    color: var(--ink-soft); font-size: 14px; white-space: nowrap;
  }
  .email-submit {
    width: 69px; display: flex; align-items: center; justify-content: center;
    color: #fff; font-size: 13px;
    background: linear-gradient(180deg, var(--accent) 0%, var(--accent-dark) 100%);
  }

  .cloud { position: absolute; overflow: visible; }
  .cloud path { fill: var(--paper); stroke: var(--line); stroke-width: 1.2; vector-effect: non-scaling-stroke; }
  .cloud-text {
    position: absolute; text-align: center; color: var(--accent); white-space: nowrap;
  }
  .cloud-text--delivery { left: 27px; top: 30px; width: 179px; font-size: 13.5px; line-height: 1.4; }
  .cloud-text--price { left: 136px; top: 40px; width: 183px; }
  .price-big { display: block; font-size: 24px; line-height: 1.2; }
  .price-small { display: block; font-size: 14px; line-height: 1.4; }
</style>
</head>
<body>

<section class="banner banner--invite">
  <h1 class="invite-title">Пригласите друга</h1>
  <p class="invite-subtitle">получите бонус на следующую покупку!</p>
  <div class="photo photo--kids" role="img" aria-label="Фото: девочка в красной юбке и мальчик в полосатой рубашке"></div>
  <div class="email-form">
    <div class="email-field">Введите адрес электронной почты</div>
    <div class="email-submit">послать</div>
  </div>
</section>

<section class="banner banner--delivery">
  <svg class="cloud" style="left:27px;top:11px;width:179px;height:123px" viewBox="0 0 180 125" preserveAspectRatio="none">
    <path d="M30,95 a22,22 0 0,1 -5,-40 a28,28 0 0,1 40,-35 a30,30 0 0,1 50,-5 a28,28 0 0,1 40,25 a22,22 0 0,1 -5,45 a26,26 0 0,1 -40,15 a30,30 0 0,1 -45,0 a26,26 0 0,1 -35,-5 z"/>
  </svg>
  <svg class="cloud" style="left:122px;top:137px;width:46px;height:33px" viewBox="0 0 180 125" preserveAspectRatio="none">
    <path d="M30,95 a22,22 0 0,1 -5,-40 a28,28 0 0,1 40,-35 a30,30 0 0,1 50,-5 a28,28 0 0,1 40,25 a22,22 0 0,1 -5,45 a26,26 0 0,1 -40,15 a30,30 0 0,1 -45,0 a26,26 0 0,1 -35,-5 z"/>
  </svg>
  <svg class="cloud" style="left:157px;top:173px;width:24px;height:21px" viewBox="0 0 180 125" preserveAspectRatio="none">
    <path d="M30,95 a22,22 0 0,1 -5,-40 a28,28 0 0,1 40,-35 a30,30 0 0,1 50,-5 a28,28 0 0,1 40,25 a22,22 0 0,1 -5,45 a26,26 0 0,1 -40,15 a30,30 0 0,1 -45,0 a26,26 0 0,1 -35,-5 z"/>
  </svg>
  <p class="cloud-text cloud-text--delivery">Доставка по<br>всей России.<br>Оплата при<br>получении.</p>
  <div class="photo photo--girl-standing" role="img" aria-label="Фото: девочка в зелёном платье с ромашками"></div>
</section>

<section class="banner banner--price">
  <div class="photo photo--girl-sitting" role="img" aria-label="Фото: сидящая девочка в зелёном платье с ромашками"></div>
  <svg class="cloud" style="left:136px;top:11px;width:183px;height:117px" viewBox="0 0 180 125" preserveAspectRatio="none">
    <path d="M30,95 a22,22 0 0,1 -5,-40 a28,28 0 0,1 40,-35 a30,30 0 0,1 50,-5 a28,28 0 0,1 40,25 a22,22 0 0,1 -5,45 a26,26 0 0,1 -40,15 a30,30 0 0,1 -45,0 a26,26 0 0,1 -35,-5 z"/>
  </svg>
  <svg class="cloud" style="left:177px;top:139px;width:46px;height:33px" viewBox="0 0 180 125" preserveAspectRatio="none">
    <path d="M30,95 a22,22 0 0,1 -5,-40 a28,28 0 0,1 40,-35 a30,30 0 0,1 50,-5 a28,28 0 0,1 40,25 a22,22 0 0,1 -5,45 a26,26 0 0,1 -40,15 a30,30 0 0,1 -45,0 a26,26 0 0,1 -35,-5 z"/>
  </svg>
  <svg class="cloud" style="left:164px;top:177px;width:22px;height:20px" viewBox="0 0 180 125" preserveAspectRatio="none">
    <path d="M30,95 a22,22 0 0,1 -5,-40 a28,28 0 0,1 40,-35 a30,30 0 0,1 50,-5 a28,28 0 0,1 40,25 a22,22 0 0,1 -5,45 a26,26 0 0,1 -40,15 a30,30 0 0,1 -45,0 a26,26 0 0,1 -35,-5 z"/>
  </svg>
  <p class="cloud-text cloud-text--price">
    <span class="price-big">Гарантия</span>
    <span class="price-small">лучшей цены!</span>
  </p>
</section>

</body>
</html>
```